Homepage Redesign - Hi-tech business Law Firm

I'm looking for an updated graphic design (pdf file) for the homepage of dorvantlegal.ca (and which will form the general template of the other pages - but you don't need to design that). Detailed specs are in the Word file.

Deliverable is 1 pdf file that I find good looking, that sets forth the layout of the new page.

Target Market(s)

Sophisticated customers

Industry/Entity Type

Legal

Number of Pages Required

1 page

Requirements
Nice to have
• For a main background, tech type images to do with high powered boardrooms, computers, graphs, numbers, high tech manufacturing lines etc. Also, I tend to like blues and light greys, and uploaded a file today that shows my generally preferred layout, which a few of you have been getting close to.
Should not have
• Any mention of 'Personal Injury,' backgrounds that include books, or buildings with roman columns. Page should not be in dark colors or harsh on the eyes.

```html
<!DOCTYPE html>
<html lang="en">
<head>
<meta charset="utf-8">
<title>Dorvant Legal — Home</title>
<link rel="stylesheet" href="https://fonts.googleapis.com/css2?family=Figtree:wght@400;500;600&display=swap">
<style>
:root{
  --bar:#eef2f7;
  --panel:#f1f5fa;
  --field:#ffffff;
  --line:#cfd8e3;
  --blue:#0b5c9f;
  --blue-bright:#0a78c8;
  --blue-title:#1d5f9f;
  --ink:#111418;
  --body:#3f4752;
  --muted:#5a6270;
  --card:#e7ecf3;
  --band:#e6ebf2;
  --cta-a:#4b8bcf;
  --cta-b:#2f6fb3;
  --footer:#e9eef4;
  --white:#ffffff;
}
*{box-sizing:border-box;margin:0;padding:0}
html,body{width:1200px;height:2626px;overflow:hidden}
body{font-family:"Figtree",sans-serif;color:var(--ink);background:var(--white);position:relative}
.btn{display:inline-flex;align-items:center;justify-content:center;font-size:13px;font-weight:500}

/* top bar */
.topbar{position:absolute;left:0;top:0;width:1200px;height:38px;background:var(--bar);color:var(--muted);font-size:13px;display:flex;align-items:center;justify-content:center;gap:6px}
.topbar a{color:var(--blue);text-decoration:underline}
.topbar b{color:var(--ink);font-weight:500}

/* header */
.header{position:absolute;left:0;top:38px;width:1200px;height:84px;border-bottom:2px solid #e2e5ea;background:#fff}
.brand{position:absolute;left:77px;top:20px;display:flex;align-items:center;gap:9px}
.brand-square{width:44px;height:44px;background:var(--blue)}
.brand-name{font-size:17px;font-weight:500;letter-spacing:2.5px;color:#2a3442;line-height:1.1;text-transform:uppercase}
.nav{position:absolute;left:281px;top:32px;display:flex;gap:21px;font-size:13px;color:#3b4350}
.search{position:absolute;left:771px;top:22px;width:236px;height:39px;border:2px solid #dfe2e7;font-size:13px;color:#535b67;padding:10px 15px}
.search svg{position:absolute;right:14px;top:11px}
.btn-contact{position:absolute;left:1021px;top:23px;width:104px;height:37px;background:var(--blue-bright);color:#fff}

/* hero */
.hero{position:absolute;left:0;top:122px;width:1200px;height:480px;background:#fff;overflow:hidden}
.hero-tech{position:absolute;left:470px;top:0;width:730px;height:480px;background:linear-gradient(90deg,#ffffff 0%,#eef2f6 25%,#dde4ec 60%,#ccd6e1 100%)}
.hero-tech svg{position:absolute;left:0;top:0}
.hero-portrait{position:absolute;left:680px;top:40px;width:370px;height:440px;background:linear-gradient(180deg,#7a7d83 0%,#3a3f48 45%,#262a32 100%);border-radius:150px 150px 0 0}
.hero h1{position:absolute;left:161px;top:128px;font-size:40px;font-weight:500;line-height:43px;letter-spacing:-0.8px;color:var(--ink)}
.hero h1 span{color:var(--blue-title)}
.hero p{position:absolute;left:161px;top:236px;width:450px;font-size:13px;line-height:17px;color:#454c57}
.btn-read{position:absolute;left:161px;top:297px;width:115px;height:37px;background:var(--blue);color:#fff}
.btn-video{position:absolute;left:291px;top:296px;width:130px;height:39px;border:2px solid var(--blue);color:var(--blue);gap:8px;background:#fff}
.hero-chev{position:absolute;left:591px;top:424px}

/* evaluation */
.eval{position:absolute;left:0;top:602px;width:1200px;height:638px;background:var(--panel);color:var(--ink)}
.eval h2.small{position:absolute;left:163px;top:88px;font-size:22px;font-weight:500;letter-spacing:-0.3px}
.form{position:absolute;left:162px;top:134px;width:323px;height:384px;border:2px solid var(--line);background:#fff}
.form-intro{position:absolute;left:14px;top:14px;width:260px;font-size:13px;line-height:17px;color:var(--body)}
.field{position:absolute;background:var(--panel);border:1px solid #dde4ec;color:var(--muted);font-size:13px;padding:10px 15px}
.form-note{position:absolute;left:22px;top:276px;width:285px;font-size:12.5px;line-height:17px;color:var(--body)}
.btn-submit{position:absolute;left:14px;top:326px;width:115px;height:37px;background:var(--blue);color:#fff}
.eval h2.big{position:absolute;left:527px;top:88px;width:470px;font-size:30px;font-weight:500;line-height:32px;letter-spacing:-0.5px}
.eval-copy{position:absolute;left:527px;top:212px;width:515px;font-size:13px;line-height:17px;color:var(--body)}
.eval-copy p+p{margin-top:15px}
.badge-box{position:absolute;left:527px;top:446px;width:513px;height:138px;background:#fff;border:1px solid #dde4ec}
.badge-a{position:absolute;left:20px;top:26px;width:158px;height:30px;border-radius:4px;background:#c9d3df}
.badge-b{position:absolute;left:20px;top:68px;width:138px;height:38px;border-radius:4px;background:#c7303a}
.badge-text{position:absolute;left:200px;top:34px;width:295px;font-size:12.5px;line-height:17px;color:var(--ink)}

/* news */
.news{position:absolute;left:0;top:1240px;width:1200px;height:440px;background:#fff}
.news h2{position:absolute;left:0;width:1200px;top:77px;text-align:center;font-size:22px;font-weight:500;line-height:24px;letter-spacing:-0.3px}
.card{position:absolute;top:154px;width:280px;height:170px;background:var(--card);padding:26px 23px}
.card h3{font-size:15px;font-weight:500;line-height:16px;color:var(--blue-title);margin-bottom:15px}
.card p{font-size:12.5px;line-height:17px;color:var(--muted)}
.arrow{position:absolute;top:228px}
.btn-news{position:absolute;left:542px;top:355px;width:115px;height:37px;background:var(--blue);color:#fff}

/* testimonials */
.testi{position:absolute;left:0;top:1680px;width:1200px;height:410px;background:var(--band);overflow:hidden}
.testi h2{position:absolute;left:0;width:1200px;top:48px;text-align:center;font-size:22px;font-weight:500;letter-spacing:-0.3px}
.testi .lead{position:absolute;left:0;width:1200px;top:94px;text-align:center;font-size:12.5px;line-height:17px;color:var(--muted)}
.quote{position:absolute;top:162px;height:204px;background:#fff;font-size:12.5px;line-height:17px;color:var(--body)}
.quote .rule{position:absolute;height:2px;background:#c3cad4;width:97px}
.quote .who{position:absolute;font-size:12.5px;color:var(--muted)}

/* cta */
.cta{position:absolute;left:0;top:2090px;width:1200px;height:316px;background:radial-gradient(ellipse at 50% 45%,var(--cta-a) 0%,var(--cta-b) 100%);color:#fff;text-align:center}
.cta h2{position:absolute;left:0;width:1200px;top:92px;font-size:22px;font-weight:500;letter-spacing:-0.3px}
.cta p{position:absolute;left:395px;width:410px;top:144px;font-size:12.5px;line-height:17px;color:#eef4fb}
.btn-cta{position:absolute;left:542px;top:211px;width:115px;height:37px;background:#fff;color:var(--ink)}

/* footer */
.footer{position:absolute;left:0;top:2406px;width:1200px;height:220px;background:var(--footer);color:var(--ink)}
.footer .brand{left:165px;top:87px}
.footer .brand-square{width:48px;height:48px}
.footer .brand-name{font-size:19px}
.fcol{position:absolute;top:70px;font-size:12.5px;line-height:22px;color:var(--muted)}
.fcol h4{font-size:12.5px;font-weight:600;color:var(--ink)}
.social{position:absolute;left:966px;top:98px;display:flex;gap:21px}
.social span{width:16px;height:16px;border:2px solid var(--blue-bright);border-radius:50%}
</style>
</head>
<body>

<div class="topbar">Lorem ipsum dolor sit amet consectetur &nbsp;-&nbsp; <a>adrian@dorvantlegal.ca</a> or <b>647.555.0142</b></div>

<header class="header">
  <div class="brand"><div class="brand-square"></div><div class="brand-name">Dorvant<br>Legal</div></div>
  <nav class="nav"><span>Practice Areas</span><span>About</span><span>News</span><span>Resources</span><span>Contact</span></nav>
  <div class="search">How can we help?
    <svg width="14" height="14" viewBox="0 0 14 14" fill="none" stroke="#333" stroke-width="1.6"><circle cx="6" cy="6" r="4.5"/><path d="M9.5 9.5L13 13"/></svg>
  </div>
  <a class="btn btn-contact">Contact</a>
</header>

<section class="hero">
  <div class="hero-tech" role="img" aria-label="Light grey-blue backdrop of glass towers with faint data charts">
    <svg width="730" height="480" viewBox="0 0 730 480" fill="none">
      <g stroke="#b9c6d5" stroke-width="1" opacity=".7">
        <path d="M120 0V480M240 0V480M360 0V480M480 0V480M600 0V480M720 0V480"/>
        <path d="M0 80H730M0 160H730M0 240H730M0 320H730M0 400H730"/>
      </g>
      <path d="M140 380L210 330L280 350L350 270L420 290L500 200L580 230L660 140L730 160" stroke="#7fa3c8" stroke-width="2"/>
      <g fill="#c3cfdc">
        <rect x="600" y="300" width="22" height="180"/><rect x="630" y="250" width="22" height="230"/><rect x="660" y="320" width="22" height="160"/><rect x="690" y="220" width="22" height="260"/>
      </g>
    </svg>
  </div>
  <div class="hero-portrait" role="img" aria-label="Portrait of the founding lawyer in a dark suit"></div>
  <h1>Where Innovation Meets<br>Litigation: <span>Dorvant Legal.</span></h1>
  <p>Your Legal Ally for Complex Cases. Personalized Solutions, Proven Results, and the Guidance of Founder Adrian. Schedule Your Consultation Today.</p>
  <a class="btn btn-read">Read More</a>
  <a class="btn btn-video"><svg width="16" height="14" viewBox="0 0 16 14" fill="none" stroke="#0b5c9f" stroke-width="1.5"><rect x="1" y="1" width="14" height="12"/><path d="M6 4.5v5l4-2.5z"/></svg>Video Library</a>
  <svg class="hero-chev" width="18" height="10" viewBox="0 0 18 10" fill="none" stroke="#0b5c9f" stroke-width="2"><path d="M1 1l8 7 8-7"/></svg>
</section>

<section class="eval">
  <h2 class="small">Case Evaluation</h2>
  <div class="form">
    <p class="form-intro">Fill out this form to schedule your initial consultation with our lawyers</p>
    <div class="field" style="left:14px;top:66px;width:142px;height:38px">First Name</div>
    <div class="field" style="left:166px;top:66px;width:142px;height:38px">Last Name</div>
    <div class="field" style="left:14px;top:112px;width:142px;height:38px">Email</div>
    <div class="field" style="left:166px;top:112px;width:142px;height:38px">Phone</div>
    <div class="field" style="left:14px;top:158px;width:294px;height:99px">Case Details</div>
    <p class="form-note">*By using this site and or submitting this form, I agree to the Privacy Policy and Terms of Use.</p>
    <a class="btn btn-submit">Submit Form</a>
  </div>
  <h2 class="big">Your Experienced Toronto and Hamilton Lawyers – Getting the Results That Matter</h2>
  <div class="eval-copy">
    <p>Dorvant Legal is a boutique litigation firm with law offices in Toronto and Hamilton. We concentrate our legal practice on complex business litigation, professional negligence (malpractice) claims, and insurance coverage disputes. We take an innovative approach to our client’s legal problems, and are guided by the philosophy that our job is to get results.</p>
    <p>The lawyers at Dorvant Legal have the reputation for vigorously representing their clients’ interests and competing hard to obtain the best possible results. With experience at all stages of legal disputes, the lawyers at Dorvant Legal are equally at home negotiating in a boardroom or presenting a case at trial. We hope that you take the time to explore our website to find out how our record of excellence, expertise and many years of experience can assist you.</p>
  </div>
  <div class="badge-box">
    <div class="badge-a"></div>
    <div class="badge-b"></div>
    <p class="badge-text">An excellent rating for a lawyer with some experience. This rating indicates the attorney is widely respected by their peers for high professional achievement and ethical standards.</p>
  </div>
</section>

<section class="news">
  <h2>News and Media Appearances<br>by - Adrian Vellacourt</h2>
  <svg class="arrow" style="left:106px" width="26" height="16" viewBox="0 0 26 16" fill="none" stroke="#111" stroke-width="2"><path d="M25 8H2M9 1L2 8l7 7"/></svg>
  <article class="card" style="left:163px"><h3>Metro Current News Story on Technology in the Courts</h3><p>Nora Calloway interviewed the Chief Justice of Ontario along with Adrian Vellacourt on the efforts by the Ontario court system to modernize in the face...</p></article>
  <article class="card" style="left:461px"><h3>Buyer beware when it comes to hiring a contractor for household renovations</h3><p>Lorem ipsum dolor sit amet consectetur. Tellus vitae auctor tristique at ut eros. Sit pellentesque e...</p></article>
  <article class="card" style="left:758px"><h3>In Small Claims Court,<br>Justice Delayed</h3><p>Lorem ipsum dolor sit amet consectetur. Lacus nibh cras suscipit bibendum arcu tincidunt. Enim eget pulvinar iaculis facilisis ac porttitor.</p></article>
  <svg class="arrow" style="left:1067px" width="26" height="16" viewBox="0 0 26 16" fill="none" stroke="#111" stroke-width="2"><path d="M1 8h23M17 1l7 7-7 7"/></svg>
  <a class="btn btn-news">More News</a>
</section>

<section class="testi">
  <h2>Testimonials</h2>
  <p class="lead">Our team of skilled attorneys is dedicated to<br>providing you with the legal expertise you deserve.</p>
  <div class="quote" style="left:-10px;width:325px;padding:60px 50px 0 10px">nsectetur. Lacus massa mattis laoreet eu tempor. Vitae facilisis nunc sodales ultricies nibh platea diam natoque ut.
    <div class="rule" style="left:10px;top:128px"></div><div class="who" style="left:20px;top:144px">Pedro Lucky</div></div>
  <div class="quote" style="left:332px;width:536px;padding:52px 42px 0 42px">“ Exceptional service from Dorvant Legal! Their expert guidance and personalized approach made a daunting legal process surprisingly smooth. I’m grateful for their 24/7 support and transparent communication. Highly recommend for anyone navigating family law matters! ”
    <div class="rule" style="left:218px;top:136px"></div><div class="who" style="left:0;width:536px;text-align:center;top:152px">Emily. W</div></div>
  <div class="quote" style="left:886px;width:330px;padding:60px 0 0 42px;white-space:nowrap;overflow:hidden">Lorem ipsum dolor sit amet consectetur. Lacus<br>molestie viverra tristique eget tempor. Vitae fa<br>nisl risus. Aliquam laoreet arcu nibh platea dia
    <div class="rule" style="left:218px;top:128px"></div><div class="who" style="left:241px;top:144px">Jan Kylie</div></div>
</section>

<section class="cta" role="img" aria-label="Soft blue backdrop with gentle light">
  <h2>Schedule a Free Consultation</h2>
  <p>Trust our seasoned experience to guide you through complex legal challenges. Our dedicated team of skilled attorneys is committed to providing the expertise you deserve.</p>
  <a class="btn btn-cta">Contact</a>
</section>

<footer class="footer">
  <div class="brand"><div class="brand-square"></div><div class="brand-name">Dorvant<br>Legal</div></div>
  <div class="fcol" style="left:465px"><h4>Company</h4>About<br>Attorneys<br>Practice Areas</div>
  <div class="fcol" style="left:630px"><h4>Other</h4>Blog<br>FAQs<br>For Clients</div>
  <div class="fcol" style="left:773px"><h4>Other</h4>Blog<br>FAQs<br>For Clients</div>
  <div class="fcol" style="left:958px"><h4>Find us on</h4></div>
  <div class="social"><span></span><span></span><span></span></div>
</footer>

</body>
</html>
```